I need a design for Corvane Homes which is a custom home builder. The name on it will be Dan Hartley, and I will give the phone number to the winning design. No address or website needed.

```html
<!DOCTYPE html>
<html lang="en">
<head>
<meta charset="utf-8">
<title>Corvane Homes – Business Card</title>
<link rel="stylesheet" href="https://fonts.googleapis.com/css2?family=Open+Sans:wght@400;600&display=swap">
<style>
  :root {
    --backdrop: #d4d4d4;
    --brand-red: #d21f26;
    --card-white: #ffffff;
    --ink: #1a1a1a;
    --blush: #f6e0da;
    --card-shadow: rgba(0, 0, 0, 0.22);
  }
  * { box-sizing: border-box; margin: 0; padding: 0; }
  html, body {
    width: 1200px;
    height: 985px;
    overflow: hidden;
  }
  body {
    background: var(--backdrop);
    font-family: "Open Sans", Arial, sans-serif;
    position: relative;
  }
  .card {
    position: absolute;
    left: 280px;
    width: 640px;
    height: 366px;
    border-radius: 26px;
    overflow: hidden;
    box-shadow: 0 10px 26px var(--card-shadow);
  }
  .card--front { top: 70px; background: var(--brand-red); }
  .card--back  { top: 530px; background: var(--card-white); }

  .card__decor {
    position: absolute;
    left: 0; top: 0;
    width: 100%; height: 100%;
  }

  .brand {
    position: absolute;
    right: 44px;
    bottom: 54px;
    display: flex;
    align-items: center;
    gap: 14px;
    font-size: 40px;
    font-weight: 400;
    letter-spacing: 0.5px;
    line-height: 1;
  }
  .brand__dot {
    width: 26px; height: 26px;
    border-radius: 50%;
  }
  .card--front .brand { color: var(--card-white); }
  .card--front .brand__dot { background: var(--card-white); }
  .card--back .brand { color: var(--brand-red); }
  .card--back .brand__dot { background: var(--brand-red); }

  .contact {
    position: absolute;
    left: 0;
    top: 26px;
    display: flex;
    gap: 12px;
  }
  .contact__marker {
    width: 30px; height: 30px;
    background: var(--brand-red);
  }
  .contact__text { color: var(--ink); }
  .contact__name {
    font-size: 25px;
    font-weight: 400;
    line-height: 30px;
  }
  .contact__phone {
    font-size: 22px;
    font-weight: 400;
    letter-spacing: 1.5px;
    line-height: 28px;
  }
</style>
</head>
<body>
  <section class="card card--front" aria-label="Card front">
    <svg class="card__decor" viewBox="0 0 640 366" aria-hidden="true">
      <circle cx="300" cy="150" r="190" fill="none" stroke="#ffffff" stroke-opacity="0.08" stroke-width="14"/>
    </svg>
    <div class="brand">
      <span class="brand__dot"></span>
      <span class="brand__name">Corvane Homes</span>
    </div>
  </section>

  <section class="card card--back" aria-label="Card back">
    <svg class="card__decor" viewBox="0 0 640 366" aria-hidden="true">
      <circle cx="260" cy="190" r="200" fill="none" stroke="var(--blush)" stroke-width="16"/>
      <line x1="0" y1="250" x2="640" y2="150" stroke="#e6e6e6" stroke-width="6"/>
    </svg>
    <div class="contact">
      <span class="contact__marker"></span>
      <div class="contact__text">
        <p class="contact__name">Dan Hartley</p>
        <p class="contact__phone">000 000 000</p>
      </div>
    </div>
    <div class="brand">
      <span class="brand__dot"></span>
      <span class="brand__name">Corvane Homes</span>
    </div>
  </section>
</body>
</html>
```